Update current boring label!!

Help! We need to have our current label redesigned. Initially it was ok but now it needs more punch. We have 3 different products. Vinaigrettes, Balsamic Glazes, and flavored olive oils. I want the same label for all 3 but perhaps in different colors to set the 3 apart. I like clean lines and need something that will be easier to read. Colors I like are black, white, golds, greens and browns.

I like some of the olive oil labels that are out there as they are very clear and easy to read. Same holds true with some Champagne labels.

You all have been so terrific in the past I hope someone can generate a new and wonderful look.

I have attached the current label to use for size.

I look forward to seeing all your wonderful designs.
Updates

Designers,I went on framevault and asked to see all the olive oil labels and there were many labels that I liked a lot. The vintage look is amazing, so please check them out to get an overall feel for what we are looking for.Many thanks,Lorna Added Wednesday, August 9, 2017

Reason: I feel like the label still needs some work. Am looking for that design that without tasting our product SELLS IT!

Target Market(s)

Upscale food buyers. Our products are on the upper end of the spectrum and cost a bit more than others due to their high quality ingredients

Font styles to use
Serif
Decorative
Script

Colors

Designer to choose colors to be used in the design.

Requirements
Must have
• A label that stands out. I see all the wonderful labels that are out there and want something that looks like it's worth more money.
• I would like Marlow to be have more of a punch as well.
Nice to have
• I like the look of white labels with wonderful designs that are easy to read and really stand out. Right now our product is basically plain. The look of champagne labels and olive oil labels. You can get a feel for what I am looking for by looking on line at the different types of labels on bottles.
Should not have
• No pictures just print

```html
<!DOCTYPE html>
<html lang="en">
<head>
<meta charset="utf-8">
<title>Marlow Champagne Pears Vinaigrette Label</title>
<link rel="stylesheet" href="https://fonts.googleapis.com/css2?family=Marcellus&family=Dancing+Script:wght@500&family=Josefin+Sans:wght@400;600&display=block">
<style>
  :root {
    --backdrop: #a9b6bf;
    --paper: #ffffff;
    --brown: #5a3418;
    --slate: #2f3a44;
    --gold: #e9b24c;
    --copper-dark: #7a3d14;
    --copper-mid: #c8763a;
    --copper-light: #f6d18a;
    --panel: #131313;
    --olive-dark: #5f6e1e;
    --olive-light: #9aa83a;
  }
  html, body {
    margin: 0;
    padding: 0;
    width: 840px;
    height: 1200px;
    overflow: hidden;
    background: radial-gradient(ellipse at 50% 40%, #c9d3da 0%, var(--backdrop) 100%);
  }
  .label {
    position: absolute;
    left: 237px;
    top: 60px;
    width: 366px;
    height: 1080px;
    display: block;
  }
  .brand-name { font-family: "Marcellus", serif; font-size: 58px; fill: var(--brown); }
  .tagline { font-family: "Josefin Sans", sans-serif; font-weight: 600; font-size: 11.5px; fill: var(--brown); letter-spacing: 0.3px; }
  .flavour { font-family: "Dancing Script", cursive; font-weight: 500; font-size: 64px; fill: var(--brown); }
  .product-type { font-family: "Josefin Sans", sans-serif; font-weight: 600; font-size: 33px; fill: var(--slate); letter-spacing: 1.5px; }
  .volume { font-family: "Josefin Sans", sans-serif; font-weight: 400; font-size: 27px; fill: var(--gold); }
</style>
</head>
<body>
<svg class="label" viewBox="0 0 366 1080" xmlns="http://www.w3.org/2000/svg">
  <defs>
    <linearGradient id="copper" x1="0" y1="0" x2="1" y2="1">
      <stop offset="0" stop-color="var(--copper-light)"/>
      <stop offset="0.35" stop-color="var(--copper-mid)"/>
      <stop offset="0.6" stop-color="var(--copper-dark)"/>
      <stop offset="0.85" stop-color="var(--copper-light)"/>
      <stop offset="1" stop-color="var(--copper-mid)"/>
    </linearGradient>
    <radialGradient id="sprig-tone" cx="0.5" cy="0.55" r="0.65">
      <stop offset="0" stop-color="var(--olive-light)" stop-opacity="0.55"/>
      <stop offset="0.6" stop-color="var(--olive-dark)" stop-opacity="0.35"/>
      <stop offset="1" stop-color="var(--panel)" stop-opacity="0"/>
    </radialGradient>
  </defs>

  <path class="label-edge" fill="url(#copper)"
        d="M0,1080 V150 Q0,138 12,138 H32 V128 A151 128 0 0 1 334 128 V138 H354 Q366 138 366 150 V1080 Z"/>
  <path class="label-paper" fill="var(--paper)"
        d="M6,1074 V152 Q6,144 14,144 H38 V130 A145 122 0 0 1 328 130 V144 H352 Q360 144 360 152 V1074 Z"/>
  <path class="label-inner-rule" fill="none" stroke="var(--gold)" stroke-width="2"
        d="M14,1066 V158 H46 V132 A137 114 0 0 1 320 132 V158 H352 V1066 Z"/>

  <circle class="brand-dot" cx="183" cy="96" r="24" fill="var(--brown)"/>
  <text class="brand-name" x="183" y="232" text-anchor="middle">Marlow</text>
  <text class="tagline" x="183" y="283" text-anchor="middle">WONDERFULLY INDULGE DRESSING</text>
  <line x1="72" y1="288" x2="294" y2="288" stroke="var(--brown)" stroke-width="1"/>
  <rect role="img" aria-label="Small scroll flourish divider" x="110" y="300" width="146" height="4" rx="2" fill="var(--brown)" opacity="0.8"/>

  <text class="flavour" x="183" y="402" text-anchor="middle">Champagne</text>
  <text class="flavour" x="183" y="476" text-anchor="middle">Pears</text>
  <rect role="img" aria-label="Scroll flourish divider" x="40" y="515" width="286" height="4" rx="2" fill="var(--brown)" opacity="0.85"/>
  <text class="product-type" x="183" y="577" text-anchor="middle">VINAIGRETTE</text>

  <rect class="panel-band" x="14" y="612" width="338" height="6" fill="url(#copper)"/>
  <rect class="panel" x="14" y="618" width="338" height="448" fill="var(--panel)"/>
  <rect class="panel-rule" x="26" y="630" width="314" height="424" fill="none" stroke="url(#copper)" stroke-width="2.5"/>
  <rect x="30" y="634" width="306" height="416" fill="none" stroke="var(--gold)" stroke-width="0.8" opacity="0.7"/>

  <rect class="sprig-area" role="img" aria-label="Illustration of a sprig of green olives with leaves hanging from a brown stem"
        x="34" y="638" width="298" height="280" fill="url(#sprig-tone)"/>

  <text class="volume" x="183" y="988" text-anchor="middle">8.5 FL OZ</text>
  <text class="volume" x="183" y="1030" text-anchor="middle">250 ml</text>
</svg>
</body>
</html>
```